Portrait of a Graduate

Our school community has created a document which describes the characteristics that every student who graduates from our school should possess. We would like a visual graphic to present the information to parents\ community. We came up with three buckets (Personal, Social, and Academic) and the concept "BRN Graduates Will Be Okay" is the central theme.
We are open to 2 different concepts:
1. A ven diagram of sorts, where the three buckets are each in an area - and the over lap is "BRN Graduates Will Be Okay"
2. Our logo has a sassafras leaf in it - using the leaves to represent each bucket and the central concept as the stem - or some other creative version.

The text to be used is below:

BRN Graduates Will Be Okay (at the center/on the stem)

1. Personal
They will:
have self-worth
advocate for themselves
feel secure in their future

2. Social
They will:
embrace differences
engage in trusting relationships
be compassionate (members of their community)

3. Academic
They will:
apply skills and strategies
creatively problem-solve
achieve individual success

```html
<!DOCTYPE html>
<html lang="en">
<head>
<meta charset="utf-8">
<title>Portrait of a Graduate – Brennan Ridge School</title>
<link rel="stylesheet" href="https://fonts.googleapis.com/css2?family=Crimson+Pro:wght@400;700&display=swap">
<style>
  :root {
    --paper: #ffffff;
    --navy: #2c3a4c;
    --gold: #cfb841;
    --forest: #344f33;
    --navy-gold: #465365;
    --navy-forest: #50684d;
    --gold-forest: #e2cf84;
    --ink: #2c3a4c;
    --on-dark: #f2f0e8;
    --on-gold: #33362f;
  }
  * { margin: 0; padding: 0; box-sizing: border-box; }
  html, body {
    width: 1200px;
    height: 1136px;
    overflow: hidden;
    background: var(--paper);
  }
  .portrait {
    width: 1200px;
    height: 1136px;
    display: block;
  }
  .portrait text { font-family: "Crimson Pro", Georgia, serif; }
  .theme-title {
    font-size: 50px;
    fill: var(--ink);
    letter-spacing: 3px;
  }
  .bucket-title { font-size: 25px; font-weight: 700; letter-spacing: 0.5px; }
  .bucket-lead { font-size: 21px; letter-spacing: 0.5px; }
  .trait { font-size: 20px; letter-spacing: 0.4px; }
  .trait-note { font-size: 13px; letter-spacing: 0.3px; }
  .on-dark { fill: var(--on-dark); }
  .on-gold { fill: var(--on-gold); }
  .on-light { fill: var(--ink); }
  .school-name { font-size: 26px; fill: var(--ink); letter-spacing: 1.5px; }
  .school-rule { stroke: var(--gold); stroke-width: 1.5; }
  .school-dot { fill: var(--ink); }
</style>
</head>
<body>
<svg class="portrait" viewBox="0 0 1988 1880" preserveAspectRatio="xMidYMid meet" xmlns="http://www.w3.org/2000/svg">
  <defs>
    <clipPath id="clip-personal-circle"><circle cx="1007" cy="810" r="260"/></clipPath>
    <clipPath id="clip-academic-circle"><circle cx="872" cy="1012" r="260"/></clipPath>
    <clipPath id="clip-social-circle"><circle cx="1142" cy="1012" r="260"/></clipPath>
    <path id="theme-arc" d="M 697 820 A 312 312 0 0 1 1321 820"/>
  </defs>

  <!-- Theme heading -->
  <text class="theme-title">
    <textPath href="#theme-arc" startOffset="50%" text-anchor="middle">BRN GRADUATES WILL BE OKAY</textPath>
  </text>

  <!-- Three buckets -->
  <g class="venn">
    <circle class="bucket personal" cx="1007" cy="810" r="260" fill="var(--navy)"/>
    <circle class="bucket academic" cx="872" cy="1012" r="260" fill="var(--gold)"/>
    <circle class="bucket social" cx="1142" cy="1012" r="260" fill="var(--forest)"/>

    <g clip-path="url(#clip-personal-circle)">
      <circle cx="872" cy="1012" r="260" fill="var(--navy-gold)"/>
      <circle cx="1142" cy="1012" r="260" fill="var(--navy-forest)"/>
    </g>
    <g clip-path="url(#clip-academic-circle)">
      <circle cx="1142" cy="1012" r="260" fill="var(--gold-forest)"/>
    </g>
    <g clip-path="url(#clip-personal-circle)">
      <g clip-path="url(#clip-academic-circle)">
        <circle cx="1142" cy="1012" r="260" fill="var(--paper)"/>
      </g>
    </g>
  </g>

  <!-- Personal traits -->
  <g class="traits personal-traits on-dark" text-anchor="middle">
    <text class="trait" x="1011" y="626">HAVE SELF-WORTH</text>
    <text class="trait" x="1011" y="673">ADVOCATE FOR THEMSELVES</text>
    <text class="trait" x="1011" y="720">FEEL SECURE IN THEIR FUTURE</text>
  </g>

  <!-- Bucket labels -->
  <g class="bucket-label personal-label on-dark" text-anchor="middle">
    <text class="bucket-title" x="841" y="847">I. PERSONAL</text>
    <text class="bucket-lead" x="841" y="871">THEY WILL:</text>
  </g>
  <g class="bucket-label social-label on-dark" text-anchor="middle">
    <text class="bucket-title" x="1172" y="857">II. SOCIAL</text>
    <text class="bucket-lead" x="1172" y="881">THEY WILL:</text>
  </g>
  <g class="bucket-label academic-label on-light" text-anchor="middle">
    <text class="bucket-title" x="1006" y="1115">III. ACADEMIC</text>
    <text class="bucket-lead" x="1006" y="1139">THEY WILL:</text>
  </g>

  <!-- Academic traits -->
  <g class="traits academic-traits on-gold" text-anchor="middle">
    <text class="trait" x="714" y="994">APPLY SKILLS AND</text>
    <text class="trait" x="714" y="1018">STRATEGIES</text>
    <text class="trait" x="741" y="1100">CREATIVELY</text>
    <text class="trait" x="741" y="1124">PROBLEM-SOLVE</text>
    <text class="trait" x="841" y="1200">ACHIEVE INDIVIDUAL</text>
    <text class="trait" x="841" y="1224">SUCCESS</text>
  </g>

  <!-- Social traits -->
  <g class="traits social-traits on-dark" text-anchor="middle">
    <text class="trait" x="1298" y="982">EMBRACE</text>
    <text class="trait" x="1298" y="1006">DIFFERENCES</text>
    <text class="trait" x="1279" y="1082">ENGAGE IN</text>
    <text class="trait" x="1279" y="1106">TRUSTING</text>
    <text class="trait" x="1279" y="1130">RELATIONSHIPS</text>
    <text class="trait" x="1180" y="1192">BE COMPASSIONATE</text>
    <text class="trait-note" x="1180" y="1210">(MEMBERS OF THEIR COMMUNITY)</text>
  </g>

  <!-- School name at the centre -->
  <g class="school-mark" text-anchor="middle">
    <circle class="school-dot" cx="1007" cy="922" r="9"/>
    <line class="school-rule" x1="917" y1="942" x2="1101" y2="942"/>
    <text class="school-name" x="1009" y="968">BRENNAN RIDGE</text>
    <text class="school-name" x="1009" y="988">SCHOOL</text>
    <line class="school-rule" x1="917" y1="996" x2="1101" y2="996"/>
  </g>
</svg>
</body>
</html>
```